Bref créative
Stationery
Health centre
Bright & Fun-filled
Meadowlark Wellness Studio
We need cards for different individuals - easily editable
12B Harlow Terrace
Carrowford
EH4 7QN
info@meadowlarkwellstudio.co.uk
www.meadowlarkwellstudio.co.uk
appointments date and time & cancelation policy.
We require 24 hours cancellation for appointments otherwise a charge may be incurred.

```html
<!DOCTYPE html>
<html lang="en">
<head>
<meta charset="utf-8">
<title>Meadowlark Wellness Studio – Stationery</title>
<link href="https://fonts.googleapis.com/css2?family=Cinzel:wght@600&family=Open+Sans:wght@400;600&display=swap" rel="stylesheet">
<style>
:root{
  --bg:#f1f2f0;
  --paper:#ffffff;
  --green:#4f8a1e;
  --green-dark:#2f6412;
  --green-light:#7bb33a;
  --ink:#555a50;
  --rule:#7aa6cf;
  --lotus:#e3ead9;
}
*{margin:0;padding:0;box-sizing:border-box}
html,body{width:1200px;height:859px;overflow:hidden}
body{background:var(--bg);position:relative;font-family:"Open Sans",Arial,sans-serif;color:var(--ink)}
.sheet{position:absolute;background:var(--paper);box-shadow:0 2px 6px rgba(0,0,0,.18);overflow:hidden}
.brand{font-family:"Cinzel",Georgia,serif;font-weight:600;color:var(--green);letter-spacing:.03em;line-height:1.15;display:flex;align-items:center;gap:6px}
.brand-dot{width:12px;height:12px;border-radius:50%;background:var(--green-light);flex:none}
.contact{position:absolute;font-style:normal;font-size:7px;line-height:1.45;border-left:1px solid var(--rule);padding-left:6px;white-space:nowrap}
.footer-band{position:absolute;left:0;right:0;bottom:0;background:linear-gradient(90deg,var(--green-dark),var(--green-light),var(--green-dark));color:#eef5e4;font-size:6px;text-align:center;display:flex;align-items:center;justify-content:center;white-space:nowrap}
.lotus{position:absolute;border-radius:50%;background:radial-gradient(circle,var(--lotus) 0%,rgba(227,234,217,.5) 60%,rgba(227,234,217,0) 72%)}

/* letterhead */
.letterhead{left:29px;top:48px;width:506px;height:744px}
.letterhead .brand{position:absolute;left:18px;top:20px;font-size:13px;width:150px}
.letterhead .contact{left:210px;top:20px}
.letterhead .lotus{left:90px;top:440px;width:320px;height:320px}
.letterhead .footer-band{height:16px;bottom:8px}

/* card front */
.card-front{left:595px;top:48px;width:221px;height:120px}
.card-front .brand{position:absolute;left:10px;top:22px;font-size:9px;width:100px}
.card-front .contact{left:114px;top:16px;font-size:5px;padding-left:5px}
.card-front .footer-band{height:10px;font-size:5px}

/* card back */
.card-back{left:833px;top:48px;width:221px;height:120px;background:radial-gradient(ellipse at 50% 40%,var(--green-light),var(--green-dark) 85%);color:#eef5e4}
.card-back .brand{position:absolute;left:0;right:0;top:10px;justify-content:center;color:#fff;font-size:8px}
.card-back .brand-dot{width:8px;height:8px;background:#fff}
.appt{position:absolute;left:50px;top:36px;width:130px;font-size:5.5px}
.appt-row{display:flex;align-items:flex-end;gap:4px;height:10px}
.appt-row span{width:18px}
.appt-row i{flex:1;border-bottom:1px solid rgba(255,255,255,.7)}
.policy{position:absolute;left:16px;right:16px;bottom:12px;text-align:center;font-size:5px;line-height:1.5}

/* envelope front */
.env-front{left:595px;top:192px;width:576px;height:312px}
.env-front .brand{position:absolute;left:22px;top:24px;font-size:14px;width:170px}
.env-front .contact{left:22px;top:232px;font-size:6.5px}
.env-front .lotus{left:330px;top:70px;width:240px;height:240px}
.env-front .footer-band{height:14px;bottom:6px}

/* envelope back */
.env-back{left:595px;top:540px;width:576px;height:288px}
.env-back svg{position:absolute;left:0;top:0}
.env-back .brand{position:absolute;left:0;right:0;top:38px;justify-content:center;color:#fff;font-size:12px}
.env-back .brand-dot{background:#fff}
</style>
</head>
<body>

<section class="sheet letterhead" aria-label="Letterhead">
  <div class="brand"><span class="brand-dot"></span>Meadowlark Wellness Studio</div>
  <address class="contact">
    12B Harlow Terrace<br>Carrowford<br>EH4 7QN<br>T: 01632 960 142<br>E: info@meadowlarkwellstudio.co.uk
  </address>
  <div class="lotus" role="img" aria-label="Faint decorative circle"></div>
  <div class="footer-band">www.meadowlarkwellstudio.co.uk</div>
</section>

<section class="sheet card-front" aria-label="Business card front">
  <div class="brand"><span class="brand-dot"></span>Meadowlark Wellness Studio</div>
  <address class="contact">
    12B Harlow Terrace<br>Carrowford<br>EH4 7QN<br>T: 01632 960 142<br>E: info@meadowlarkwellstudio.co.uk
  </address>
  <div class="footer-band">www.meadowlarkwellstudio.co.uk</div>
</section>

<section class="sheet card-back" aria-label="Appointment card back">
  <div class="brand"><span class="brand-dot"></span>Meadowlark Wellness Studio</div>
  <div class="appt">
    <div class="appt-row"><span>Day</span><i></i></div>
    <div class="appt-row"><span>Date</span><i></i></div>
    <div class="appt-row"><span>Time</span><i></i></div>
  </div>
  <p class="policy">We require 24 hours cancellation for appointments otherwise a charge may be incurred.</p>
</section>

<section class="sheet env-front" aria-label="Envelope front">
  <div class="brand"><span class="brand-dot"></span>Meadowlark Wellness Studio</div>
  <address class="contact">
    12B Harlow Terrace<br>Carrowford<br>EH4 7QN<br>T: 01632 960 142<br>E: info@meadowlarkwellstudio.co.uk
  </address>
  <div class="lotus" role="img" aria-label="Faint decorative circle"></div>
  <div class="footer-band">www.meadowlarkwellstudio.co.uk</div>
</section>

<section class="sheet env-back" aria-label="Envelope back">
  <svg width="576" height="100" viewBox="0 0 576 100" aria-hidden="true">
    <defs>
      <linearGradient id="flap" x1="0" x2="1" y1="0" y2="0">
        <stop offset="0" stop-color="#2f6412"/>
        <stop offset=".5" stop-color="#7bb33a"/>
        <stop offset="1" stop-color="#2f6412"/>
      </linearGradient>
    </defs>
    <path d="M0 0H576V62L520 92H56L0 62Z" fill="url(#flap)"/>
  </svg>
  <div class="brand"><span class="brand-dot"></span>Meadowlark Wellness Studio</div>
</section>

</body>
</html>
```